Optometrist/Eye Care Clinic Business card with new logo attached

We are a small, independent eye care clinic in Canada. We have recently updated our logo (as attached), and would like a professional, modern and health care oriented business card to highlight our office details and our optometrist. We'd like to incorporate the blue colours as seen on our logo.

Target Market(s)

demographic: age 35-65 male/female equal

Industry/Entity Type

Health Care

Contact Information for Business Card

Name of clinic: "Marrow Bend Eye Care Optometry"

Font styles to use
Sans Serif

Colors
0355a3

Requirements
Must have
• our website: marrowbendeyecare.com
• Dr Lena Quorvik
• Optometrist
• 217-392 E Halvering Ave
• Vancouver BC V6R 3J8
• P: 604-319-2058
• E: info@marrowbendeyecare.com
Nice to have
• front side: logo/name of clinic as seen on logo attached and website
• backside: logo on the left side, and name/title/address/phone/email

```html
<!DOCTYPE html>
<html lang="en">
<head>
<meta charset="utf-8">
<title>Marrow Bend Eye Care – Business Card</title>
<link rel="stylesheet" href="https://fonts.googleapis.com/css2?family=Comic+Neue:wght@700&display=swap">
<style>
  :root {
    --clinic-blue: #0355a3;
    --card-fill: #e8ebeb;
    --ink: #111111;
    --frame: #222222;
    --page: #ffffff;
  }
  * { margin: 0; padding: 0; box-sizing: border-box; }
  html, body {
    width: 1114px;
    height: 1200px;
    overflow: hidden;
    background: var(--page);
  }
  .sheet {
    position: relative;
    width: 1114px;
    height: 1200px;
    border: 1.5px solid var(--frame);
    font-family: "Comic Neue", "Comic Sans MS", sans-serif;
    font-weight: 700;
  }
  .card {
    position: absolute;
    left: 103px;
    width: 908px;
    height: 556px;
    background: var(--card-fill);
    border: 1.5px solid var(--frame);
    border-radius: 47px;
  }
  .card--front { top: 30px; }
  .card--back { top: 613px; }

  .brand-dot {
    position: absolute;
    border-radius: 50%;
    background: var(--clinic-blue);
  }
  .card--front .brand-dot { width: 94px; height: 94px; left: 407px; top: 231px; }
  .card--back .brand-dot { width: 62px; height: 62px; left: 191px; top: 98px; }

  .clinic-name {
    position: absolute;
    color: var(--clinic-blue);
    white-space: nowrap;
    letter-spacing: 1px;
  }
  .card--front .clinic-name {
    left: 0; right: 0; top: 360px;
    text-align: center;
    font-size: 52px;
  }
  .card--back .clinic-name {
    left: 25px; top: 195px;
    font-size: 34px;
  }

  .website {
    position: absolute;
    left: 0; right: 44px; top: 482px;
    text-align: center;
    font-size: 30px;
    color: var(--ink);
  }

  .contact {
    position: absolute;
    right: 47px;
    top: 305px;
    text-align: right;
    color: var(--ink);
    font-size: 25px;
    line-height: 34px;
    white-space: nowrap;
  }
  .contact__name { font-size: 38px; line-height: 44px; }
  .contact__title { font-size: 26px; }
</style>
</head>
<body>
  <div class="sheet">
    <section class="card card--front">
      <span class="brand-dot" aria-hidden="true"></span>
      <h1 class="clinic-name">MARROW BEND EYE CARE</h1>
      <p class="website">www.marrowbendeyecare.com</p>
    </section>

    <section class="card card--back">
      <span class="brand-dot" aria-hidden="true"></span>
      <h2 class="clinic-name">MARROW BEND EYE CARE</h2>
      <div class="contact">
        <p class="contact__name">Dr. Lena Quorvik</p>
        <p class="contact__title">Optometrist</p>
        <p>Add.: 217-392, E Halvering Ave,</p>
        <p>Vancouver, BC V6R 3J8.</p>
        <p>Ph.: 604-319-2058</p>
        <p>Email : info@marrowbendeyecare.com</p>
      </div>
    </section>
  </div>
</body>
</html>
```